Oil and Gas Company: Letterhead Design

In short we need a professional company letterhead designed for our Oil and Gas company.

We would like to keep the design simple and professional. Letterhead to include the company logo and color scheme, front page and continuation pages.

For reference, see attached logo below with our company logo and color scheme.

Target Market(s)

Oil & Gas Market

Industry/Entity Type

Oil And Gas

Font styles to use
Sans Serif

Requirements
Must have
• Letterhead must contain a front page & continuation page.
• Must be simple and professional in design.
• Follow our logo and color scheme.
Nice to have
• I would like to have the logo embedded in the bottom right hand portion of the page to provide some depth into the letterhead.

```html
<!DOCTYPE html>
<html lang="en">
<head>
<meta charset="utf-8">
<title>Keystone Basin Energy – Letterhead</title>
<link href="https://fonts.googleapis.com/css2?family=Mulish:wght@400;600&display=swap" rel="stylesheet">
<style>
  :root{
    --backdrop:#8c9399;
    --paper:#f3f3f3;
    --ink:#2a2a2a;
    --brand-blue:#0d4c9c;
    --brand-red:#e0141b;
    --sign-tone:#cfcfcf;
  }
  *{margin:0;padding:0;box-sizing:border-box}
  html,body{width:1200px;height:1200px;overflow:hidden}
  body{background:var(--backdrop);font-family:'Mulish',sans-serif;color:var(--ink);position:relative}
  .sheet{position:absolute;top:223px;width:525px;height:743px;background:var(--paper);overflow:hidden;box-shadow:0 2px 6px rgba(0,0,0,.25)}
  .sheet--front{left:52px}
  .sheet--continuation{left:626px}
  .band{position:absolute;display:block}
  .brand{position:absolute;display:flex;align-items:center;gap:8px;color:var(--ink)}
  .brand__mark{width:14px;height:14px;background:var(--brand-blue)}
  .brand__name{font-size:15px;font-weight:400;letter-spacing:.6px;text-transform:uppercase}
  .brand--header{left:120px;top:26px}
  .brand--footer{left:390px;top:678px;flex-direction:column;gap:4px}
  .brand--footer .brand__mark{width:12px;height:12px}
  .brand--footer .brand__name{font-size:5.6px;line-height:6.4px;text-align:center;letter-spacing:.2px}
  .copy{position:absolute;font-size:8.6px;line-height:12.8px}
  .copy p{text-align:justify;margin-bottom:12.8px}
  .copy--front{left:114px;top:95px;width:333px}
  .copy--continuation{left:114px;top:104px;width:350px}
  .address{margin-bottom:12.8px;text-align:left!important}
  .address__recipient{color:var(--brand-blue);font-weight:600}
  .closing{position:absolute;left:114px;top:530px;font-size:8.6px;line-height:12.8px}
  .signature{display:block;width:88px;height:38px;margin:6px 0 6px -12px;background:linear-gradient(90deg,var(--sign-tone),#e4e4e4);border-radius:3px}
</style>
</head>
<body>

<section class="sheet sheet--front">
  <svg class="band" style="left:0;top:0" width="525" height="7" viewBox="0 0 525 7">
    <polygon points="0,0 121,0 116,6 0,6" fill="var(--brand-blue)"/>
    <polygon points="171,0 525,0 525,6 166,6" fill="var(--brand-red)"/>
  </svg>

  <div class="brand brand--header">
    <span class="brand__mark"></span>
    <span class="brand__name">Keystone Basin Energy</span>
  </div>

  <div class="copy copy--front">
    <p class="address">August 11, 2018<br>
      <span class="address__recipient">Recipient Name</span><br>
      Company Name<br>Street Address<br>City, State, Zip Code</p>
    <p style="text-align:left">Dear Name Here,</p>
    <p>Lorem ipsum dolor sit amet, consectetur adipiscing elit, sed do eiusmod tempor incididunt ut labore et dolore magna aliqua. Ut enim ad minim veniam, quis nostrud exercitation ullamco laboris nisi ut aliquip ex ea commodo consequat. Duis aute irure dolor in reprehenderit in voluptate velit esse cillum dolore eu fugiat nulla pariatur. Excepteur sint occaecat cupidatat non proident, sunt in culpa qui officia deserunt mollit anim id est laborum.</p>
    <p>Sed ut perspiciatis unde omnis iste natus error sit voluptatem accusantium doloremque laudantium, totam rem aperiam, eaque ipsa quae ab illo inventore veritatis et quasi architecto beatae vitae dicta sunt explicabo. Nemo enim ipsam voluptatem quia voluptas sit aspernatur aut odit aut fugit, sed quia consequuntur magni dolores eos qui ratione voluptatem sequi nesciunt. Neque porro quisquam est, qui dolorem ipsum quia dolor sit amet, consectetur, adipisci velit, sed quia non numquam eius modi tempora incidunt ut labore et dolore magnam aliquam quaerat voluptatem. Ut enim ad minima veniam, quis nostrum exercitationem ullam corporis suscipit laboriosam, nisi ut aliquid ex ea commodi consequatur? Quis autem vel eum iure reprehenderit qui in ea voluptate velit esse quam nihil molestiae consequatur, vel illum qui dolorem. Excepteur sint occaecat cupidatat non proident, sunt in culpa qui officia deserunt mollit anim id est laborum.</p>
    <p>Duis aute irure dolor in reprehenderit in voluptate velit esse cillum dolore eu fugiat nulla pariatur. Excepteur sint occaecat cupidatat non proident, sunt in culpa qui officia deserunt mollit anim id est laborum. Ut enim ad minim veniam, quis nostrud exercitation ullamco laboris nisi ut aliquip ex ea commodo consequat. Duis aute irure dolor in reprehenderit in voluptate velit esse cillum dolore eu fugiat nulla pariatur. Excepteur sint occaecat cupidatat non proident, sunt in culpa qui officia deserunt mollit anim id est laborum. At vero eos et accusamus et iusto odio dignissimos ducimus qui blanditiis praesentium voluptatum deleniti atque corrupti quos dolores et quas molestias excepturi sint occaecati cupiditate non provident, similique sunt in culpa qui officia deserunt mollitia animi, id est laborum et dolorum fuga. Ut enim ad minim veniam, quis nostrud exercitation ullamco laboris nisi ut aliquip ex ea commodo consequat.</p>
    <p>Duis aute irure dolor in reprehenderit in voluptate velit esse cillum dolore eu fugiat nulla pariatur. Excepteur sint occaecat cupidatat non proident, sunt in culpa qui officia deserunt mollit anim id est laborum.</p>
  </div>

  <svg class="band" style="left:378px;top:733px" width="58" height="10" viewBox="0 0 58 10">
    <polygon points="4,0 26,0 22,10 0,10" fill="var(--brand-blue)"/>
    <polygon points="32,0 54,0 58,10 28,10" fill="var(--brand-red)"/>
  </svg>
</section>

<section class="sheet sheet--continuation">
  <svg class="band" style="left:392px;top:0" width="74" height="14" viewBox="0 0 74 14">
    <polygon points="0,0 34,0 30,13 4,13" fill="var(--brand-blue)"/>
    <polygon points="40,0 74,0 68,13 36,13" fill="var(--brand-red)"/>
  </svg>

  <div class="copy copy--continuation">
    <p>Lorem ipsum dolor sit amet, consectetur adipiscing elit, sed do eiusmod tempor incididunt ut labore et dolore magna aliqua. Ut enim ad minim veniam, quis nostrud exercitation ullamco laboris nisi ut aliquip ex ea commodo consequat. Duis aute irure dolor in reprehenderit in voluptate velit esse cillum dolore eu fugiat nulla pariatur. Excepteur sint occaecat cupidatat non proident, sunt in culpa qui officia deserunt mollit anim id est laborum.</p>
    <p>Sed ut perspiciatis unde omnis iste natus error sit voluptatem accusantium doloremque laudantium, totam rem aperiam, eaque ipsa quae ab illo inventore veritatis et quasi architecto beatae vitae dicta sunt explicabo. Nemo enim ipsam voluptatem quia voluptas sit aspernatur aut odit aut fugit, sed quia consequuntur magni dolores eos qui ratione voluptatem sequi nesciunt. Neque porro quisquam est, qui dolorem ipsum quia dolor sit amet, consectetur, adipisci velit, sed quia non numquam eius modi tempora incidunt ut labore et dolore magnam aliquam quaerat voluptatem. Ut enim ad minima veniam, quis nostrum exercitationem ullam corporis suscipit laboriosam, nisi ut aliquid ex ea commodi consequatur? Quis autem vel eum iure reprehenderit qui in ea voluptate velit esse quam nihil molestiae consequatur, vel illum qui dolorem eum fugiat quo voluptas nulla pariatur</p>
    <p>At vero eos et accusamus et iusto odio dignissimos ducimus qui blanditiis praesentium voluptatum deleniti atque corrupti quos dolores et quas molestias excepturi sint occaecati cupiditate non provident, similique sunt in culpa qui officia deserunt mollitia animi, id est laborum et dolorum fuga. Nemo enim ipsam voluptatem quia voluptas sit aspernatur aut odit aut fugit, sed quia consequuntur magni dolores eos qui ratione voluptatem sequi nesciunt. Neque porro quisquam est, qui dolorem ipsum quia dolor sit amet, consectetur, adipisci velit, sed quia non numquam eius modi tempora incidunt ut labore et dolore magnam aliquam quaerat voluptatem. Ut enim ad minima veniam, quis nostrum exercitationem ullam corporis suscipit laboriosam, nisi ut aliquid ex ea commodi consequatur? Quis autem vel eum iure reprehenderit qui in ea voluptate velit esse quam nihil molestiae consequatur, vel illum qui dolorem eum fugiat quo voluptas nulla pariatur</p>
  </div>

  <div class="closing">
    Sincerely,
    <span class="signature" role="img" aria-label="Handwritten signature of Daniel"></span>
    Daniel Hayes
  </div>

  <div class="brand brand--footer">
    <span class="brand__mark"></span>
    <span class="brand__name">Keystone Basin<br>Energy</span>
  </div>

  <svg class="band" style="left:0;top:728px" width="525" height="15" viewBox="0 0 525 15">
    <polygon points="0,6 391,6 386,15 0,15" fill="var(--brand-blue)"/>
    <polygon points="462,0 525,0 525,15 472,15" fill="var(--brand-red)"/>
  </svg>
</section>

</body>
</html>
```